Western Canadian Survey Company needs Business Card and Letter Head Design

Hello,

We're looking to have our business cards redesigned along with our letterhead.

We've recently changed out logo and would like to use this. Please use some creativity and propose different options (Traditional and modern).

We will provide as much feedback as possible.

Business card should be double sided with our logo. We would also like room for cell phone number, email address and position. Back of the card can just be our logo or potentially a list of our services we provide.

Industry/Entity Type

Business

Contact Information for Business Card

```html
<!DOCTYPE html>
<html lang="en">
<head>
<meta charset="utf-8">
<title>Ridgeline Surveys Ltd – Stationery</title>
<link rel="stylesheet" href="https://fonts.googleapis.com/css2?family=Michroma&family=Didact+Gothic&display=swap">
<style>
:root{
  --stage:#d4d4d4;
  --paper:#f0f0f0;
  --ink:#000;
  --slate:#4a5868;
  --slate-light:#8797a8;
  --text:#333;
  --white:#fff;
}
*{box-sizing:border-box;margin:0;padding:0}
html,body{width:1200px;height:1041px;overflow:hidden;background:var(--stage)}
body{position:relative;font-family:"Didact Gothic",sans-serif;color:var(--text)}
.piece{position:absolute;overflow:hidden}
.wordmark{font-family:"Michroma",sans-serif;letter-spacing:.04em;text-align:center;white-space:nowrap}
.wordmark .mark{display:inline-block;vertical-align:middle;margin-right:.5em;width:.7em;height:.7em;background:currentColor}

/* folder */
.folder{left:166px;top:76px;width:417px;height:541px;background:var(--ink);border-radius:4px}
.folder .wordmark{position:absolute;left:0;right:0;top:112px;font-size:16px;color:var(--slate-light)}
.folder .url{position:absolute;left:0;right:0;top:498px;text-align:center;font-size:8.5px;color:var(--white)}
.folder .url span{color:var(--slate-light)}

/* letterhead */
.letterhead{left:615px;top:94px;width:403px;height:523px;background:var(--paper)}
.letterhead .wordmark{position:absolute;left:0;right:0;top:56px;font-size:11px;color:var(--slate)}
.letter-body{position:absolute;left:37px;top:153px;width:330px;font-size:5.4px;line-height:1.32;text-align:justify}
.letter-body p{margin-bottom:6px}
.letter-body .greeting{font-weight:bold;color:#111;margin-bottom:8px}
.signoff{position:absolute;left:37px;top:325px;font-size:5.4px;line-height:1.45}
.signoff b{color:#111}
.signature{position:absolute;left:86px;top:322px;width:70px;height:36px;background:#dde0ea;border-radius:3px}
.footer-line{position:absolute;left:0;right:0;font-size:5.2px;text-align:center}
.rule{position:absolute;height:2px;background:var(--slate)}
.band{position:absolute;left:0;right:0;background:var(--ink)}
.url-caps{font-size:5.2px;color:var(--slate);letter-spacing:.02em;position:absolute}

/* envelope front */
.envelope-front{left:132px;top:646px;width:451px;height:195px;background:var(--paper)}
.envelope-front .wordmark{position:absolute;left:22px;top:46px;font-size:10px;color:var(--slate)}

/* envelope back */
.envelope-back{left:615px;top:646px;width:451px;height:195px;background:var(--paper)}
.envelope-back svg{position:absolute;left:0;top:0}
.envelope-back .wordmark{position:absolute;left:0;right:0;top:26px;font-size:11px;color:var(--white)}
.envelope-back .url{position:absolute;left:0;right:0;top:172px;text-align:center;font-size:5.5px;color:#222}

/* cards */
.card-front{left:416px;top:870px;width:167px;height:95px;background:var(--ink)}
.card-front .wordmark{position:absolute;left:0;right:0;top:34px;font-size:6.5px;color:var(--slate-light)}
.card-front .url{position:absolute;left:0;right:0;top:78px;text-align:center;font-size:4px;color:var(--white)}
.card-front .url span{color:var(--slate-light)}
.card-back{left:615px;top:870px;width:167px;height:95px;background:var(--paper)}
.card-back .wordmark{position:absolute;left:0;right:0;top:15px;font-size:5.5px;color:var(--slate)}
.card-back .name{position:absolute;left:0;right:0;top:47px;text-align:center;font-size:5px;font-weight:bold;color:var(--slate);letter-spacing:.05em}
.card-back .role{position:absolute;left:0;right:0;top:54px;text-align:center;font-size:3.6px}
.card-back .contact{position:absolute;left:0;right:0;top:69px;text-align:center;font-size:3.4px;line-height:1.4}
</style>
</head>
<body>

<section class="piece folder" aria-label="Presentation folder">
  <div class="wordmark"><span class="mark"></span>RIDGELINE SURVEYS</div>
  <p class="url">www.<span>ridgelinesurveys</span>.net</p>
</section>

<section class="piece letterhead" aria-label="Letterhead">
  <div class="wordmark"><span class="mark"></span>RIDGELINE SURVEYS</div>
  <div class="letter-body">
    <p class="greeting">Dear sir,</p>
    <p>Communication sits at the centre of every project we take on. Clear notes, timely updates and accurate records keep crews, clients and engineers working from the same information on every site.</p>
    <p>In a world of quick messages and shared screens, a written letter still carries weight. Municipal offices, developers and lenders continue to rely on signed documents as a lasting record of scope, measurements and agreed terms. A letter remains the most trusted proof of what was said.</p>
    <p>A letter also speaks for the organisation that sends it, so care must be taken that the language suits the occasion and that nothing is left open to doubt.</p>
    <p>Please review the enclosed survey summary and contact our office with any questions. We look forward to continuing our work together.</p>
  </div>
  <div class="signoff">Yours Sincerely,<br><b>Carla Weston</b></div>
  <div class="signature" role="img" aria-label="Handwritten signature"></div>
  <p class="footer-line" style="top:485px">418 Cedar Bench Road, Vernon, BC, V1T 4K2 · <b>T:</b> +780 555 0142 · <b>E:</b> hr@ridgelinesurveys.net</p>
  <div class="rule" style="left:0;width:165px;top:501px"></div>
  <span class="url-caps" style="left:170px;top:498px">WWW.RIDGELINESURVEYS.NET</span>
  <div class="rule" style="left:242px;right:0;top:501px"></div>
  <div class="band" style="top:508px;height:7px"></div>
</section>

<section class="piece envelope-front" aria-label="Envelope front">
  <div class="wordmark"><span class="mark"></span>RIDGELINE SURVEYS</div>
  <div class="rule" style="left:0;width:26px;top:180px"></div>
  <span class="url-caps" style="left:34px;top:176px;color:#222">418 Cedar Bench Road, Vernon, BC, V1T 4K2</span>
  <div class="rule" style="left:165px;width:167px;top:180px"></div>
  <span class="url-caps" style="left:338px;top:176px">WWW.RIDGELINESURVEYS.NET</span>
  <div class="rule" style="left:434px;right:0;top:180px"></div>
  <div class="band" style="top:186px;height:7px"></div>
</section>

<section class="piece envelope-back" aria-label="Envelope back">
  <svg width="451" height="70" viewBox="0 0 451 70" aria-hidden="true">
    <path d="M0 0 H451 L435 58 Q432 64 426 64 H25 Q19 64 16 58 Z" fill="#000"/>
  </svg>
  <div class="wordmark"><span class="mark"></span>RIDGELINE SURVEYS</div>
  <p class="url">www.ridgelinesurveys.net</p>
</section>

<section class="piece card-front" aria-label="Business card front">
  <div class="wordmark"><span class="mark"></span>RIDGELINE SURVEYS</div>
  <p class="url">www.<span>ridgelinesurveys</span>.net</p>
</section>

<section class="piece card-back" aria-label="Business card back">
  <div class="wordmark"><span class="mark"></span>RIDGELINE SURVEYS</div>
  <p class="name">JORDAN ELLIS</p>
  <p class="role">General Manager</p>
  <p class="contact">418 Cedar Bench Road, Vernon, BC, V1T 4K2<br>T: +780 555 0142 · E: hr@ridgelinesurveys.net · W: www.ridgelinesurveys.net</p>
  <div class="rule" style="left:0;right:0;top:84px;height:1.5px"></div>
  <div class="band" style="top:88px;height:4px"></div>
</section>

</body>
</html>
```